Kelvane Plumbing Business cards

Company is Kelvane Plumbing.
name Dashel Morrowby, I am a plumber, drainer, gasfitter and roofer
Mobile: 0431 906 154
Email address: info@kelvaneplumbing.example (check out my website for some ideas)
Website: www.kelvaneplumbing.example
ABN: 82 916 203 471
LIC: 604517K

I am reliable all round plumber. I am a 24 hour emergency service. Kelvane Plumbing is a professional plumbing service in the Illawarra, South Coast, Southern Sydney and Southern Highland regions of NSW. We offer a 24 hour emergency service for piece of mind to our customers. Call us now to see how we can help you. Kelvane Plumbing approaches every job with attention to detail and excellent customer service. With our superior workmanship you can be confident that the job will be done right the first time around. You can rest assured with results that are guaranteed to last.

Target Market(s)

the general public

Contact Information for Business Card

look up website for some ideas something with similar colours to logo and new modern and to catch the eye.

Colors
fdfdfd
ffffff
000000
7f7f7f
aaaaaa
33a6d7
0492cd

Requirements
Must have
• all contact details
• company- Kelvane Plumbing
• name- Dashel Morrowby
• number mobile- 0431 906 154
• Email address- info@kelvaneplumbing.example
• Website- www.kelvaneplumbing.example
• ABN- 82 916 203 471
• LIC- 604517K

```html
<!DOCTYPE html>
<html lang="en">
<head>
<meta charset="utf-8">
<title>Kelvane Plumbing Business Cards</title>
<link href="https://fonts.googleapis.com/css2?family=Open+Sans:wght@400;600;700&display=swap" rel="stylesheet">
<style>
  :root {
    --card: #050505;
    --stage: #2a2a2a;
    --blue: #0492cd;
    --blue-soft: #33a6d7;
    --grey: #7f7f7f;
    --grey-light: #aaaaaa;
    --white: #fdfdfd;
  }
  * { margin: 0; padding: 0; box-sizing: border-box; }
  html, body { width: 1200px; height: 1200px; overflow: hidden; }
  body {
    background: var(--stage);
    font-family: "Open Sans", Arial, sans-serif;
    color: var(--white);
    position: relative;
  }
  .card {
    position: absolute;
    left: 160px;
    width: 880px;
    height: 538px;
    background: var(--card);
    border-radius: 22px;
    overflow: hidden;
  }
  .card--contact { top: 50px; }
  .card--brand { top: 612px; }

  /* Contact side */
  .brand-mark {
    position: absolute;
    left: 90px;
    top: 120px;
    width: 250px;
    height: 250px;
    display: flex;
    flex-direction: column;
    align-items: center;
    justify-content: center;
    gap: 14px;
  }
  .brand-mark__dot {
    width: 26px; height: 26px;
    border-radius: 50%;
    background: var(--blue);
  }
  .brand-mark__name {
    font-weight: 700;
    font-size: 30px;
    line-height: 1.15;
    letter-spacing: 1px;
    text-transform: uppercase;
    text-align: center;
    color: var(--blue);
  }
  .divider {
    position: absolute;
    left: 405px;
    top: 70px;
    width: 3px;
    height: 300px;
    background: var(--blue);
  }
  .contact {
    position: absolute;
    left: 470px;
    top: 112px;
  }
  .contact__name {
    font-weight: 700;
    font-size: 29px;
    color: var(--blue);
    text-transform: uppercase;
    letter-spacing: 0.3px;
    margin-bottom: 14px;
  }
  .contact__list { list-style: none; }
  .contact__item {
    display: flex;
    align-items: center;
    gap: 12px;
    font-size: 19px;
    line-height: 30px;
  }
  .contact__icon { width: 18px; height: 18px; flex: none; }
  .contact__reg {
    margin-top: 26px;
    margin-left: 30px;
    font-size: 19px;
    line-height: 30px;
  }
  .contact__label { color: var(--blue); font-weight: 700; }
  .services {
    position: absolute;
    left: 0; right: 0;
    bottom: 48px;
    text-align: center;
    font-weight: 700;
    font-size: 21px;
    text-transform: uppercase;
    letter-spacing: 0.3px;
  }
  .services__sep { color: var(--blue); margin: 0 8px; }

  /* Brand side */
  .wordmark {
    position: absolute;
    left: 0; right: 0;
    top: 0; bottom: 0;
    display: flex;
    align-items: center;
    justify-content: center;
    gap: 22px;
  }
  .wordmark__dot {
    width: 40px; height: 40px;
    border-radius: 50%;
    background: var(--blue);
  }
  .wordmark__name {
    font-weight: 700;
    font-size: 60px;
    letter-spacing: 3px;
    text-transform: uppercase;
    color: var(--blue);
  }
</style>
</head>
<body>

<section class="card card--contact" aria-label="Business card, contact side">
  <div class="brand-mark">
    <span class="brand-mark__dot"></span>
    <span class="brand-mark__name">Kelvane<br>Plumbing</span>
  </div>

  <div class="divider"></div>

  <div class="contact">
    <h1 class="contact__name">Dashel Morrowby</h1>
    <ul class="contact__list">
      <li class="contact__item">
        <svg class="contact__icon" viewBox="0 0 18 18"><rect x="4" y="1" width="10" height="16" rx="2" fill="none" stroke="#0492cd" stroke-width="2"/><circle cx="9" cy="14" r="1" fill="#0492cd"/></svg>
        0431 906 154
      </li>
      <li class="contact__item">
        <svg class="contact__icon" viewBox="0 0 18 18"><rect x="1" y="3.5" width="16" height="11" rx="1.5" fill="none" stroke="#0492cd" stroke-width="2"/><path d="M1.5 4.5 9 10l7.5-5.5" fill="none" stroke="#0492cd" stroke-width="2"/></svg>
        info@kelvaneplumbing.example
      </li>
      <li class="contact__item">
        <svg class="contact__icon" viewBox="0 0 18 18"><circle cx="9" cy="9" r="7.5" fill="none" stroke="#0492cd" stroke-width="1.6"/><ellipse cx="9" cy="9" rx="3.2" ry="7.5" fill="none" stroke="#0492cd" stroke-width="1.4"/><path d="M1.5 9h15M3 5h12M3 13h12" stroke="#0492cd" stroke-width="1.2"/></svg>
        www.kelvaneplumbing.example
      </li>
    </ul>
    <p class="contact__reg"><span class="contact__label">ABN:</span> 82 916 203 471<br><span class="contact__label">LIC:</span> 604517K</p>
  </div>

  <p class="services">Plumbing<span class="services__sep">•</span>Drainage<span class="services__sep">•</span>Gasfitting<span class="services__sep">•</span>Roofing</p>
</section>

<section class="card card--brand" aria-label="Business card, brand side">
  <div class="wordmark">
    <span class="wordmark__dot"></span>
    <span class="wordmark__name">Kelvane Plumbing</span>
  </div>
</section>

</body>
</html>
```